Spray Foam Company Business Card

We need a business card designed for our spray foam insulation and roof coatings business. We handle residential and commercial projects.
Industry/Entity Type
Construction
Contact Information for Business Card
We would like it to say:
K & R Coat
with these bullet points
-foam insulation
-waterproofing roof system
-water proofing foundation systems
website is krcoatfoamsealers.com (this was just purchased)
office phone : 630-555-0148
And 3 cards with names on them the names are :
Darren Hollis
Trevor Lindqvist
Neil Bruxton
maybe the bullet points can go on the back?
if you go this website it is another division of our company and you can see the font we use in the K & R. We do not want to use the same half circles that it has just the lettering
www.thesturdiestfinishwork.com
Look and feel
Each slider illustrates characteristics of the customer's brand and the style your logo design should communicate.

```html
<!DOCTYPE html>
<html lang="en">
<head>
<meta charset="utf-8">
<title>K & R Coat — Business Card</title>
<link rel="stylesheet" href="https://fonts.googleapis.com/css2?family=Open+Sans:wght@400;600;700&display=swap">
<style>
  :root {
    --page: #ffffff;
    --card-black: #000000;
    --card-white: #ffffff;
    --band-grey: #2a2a2a;
    --logo-grey: #545b63;
    --logo-faint: #2b2b2b;
    --name-red: #c8202a;
    --text-grey: #9a9a9a;
    --icon-grey: #8a8a8a;
    --shadow: rgba(0, 0, 0, 0.45);
  }
  * { box-sizing: border-box; margin: 0; padding: 0; }
  html, body {
    width: 1200px; height: 960px; overflow: hidden;
    background: var(--page);
    font-family: "Open Sans", Arial, sans-serif;
  }
  .sheet { position: relative; width: 1200px; height: 960px; }
  .card {
    position: absolute; left: 285px; width: 620px; height: 354px;
    background: var(--card-black);
    border: 1px solid #333;
    box-shadow: 6px 8px 10px var(--shadow);
    overflow: hidden;
  }
  .card--front { top: 80px; }
  .card--back { top: 501px; }

  .front__art { position: absolute; inset: 0; }
  .brand-name {
    position: absolute; font-weight: 700; letter-spacing: -0.5px; white-space: nowrap;
  }
  .card--front .brand-name { left: 26px; top: 26px; font-size: 48px; color: var(--logo-grey); }
  .person-name {
    position: absolute; right: 30px; top: 68px;
    font-size: 29px; font-weight: 700; color: var(--name-red);
  }
  .contact {
    position: absolute; left: 25px; top: 273px; list-style: none;
    color: var(--text-grey); font-size: 19px; line-height: 27px;
  }
  .contact li { display: flex; align-items: center; }
  .contact svg { width: 18px; height: 18px; margin-right: 25px; fill: var(--icon-grey); }

  .card--back .brand-name {
    left: 0; right: 0; top: 84px; text-align: center; padding-right: 40px;
    font-size: 56px; color: var(--logo-faint);
  }
  .services {
    position: absolute; left: 28px; top: 245px; list-style: none;
    color: var(--text-grey); font-size: 19px; line-height: 25.5px;
  }
  .services li::before {
    content: ""; display: inline-block; width: 4px; height: 4px; border-radius: 50%;
    background: var(--text-grey); margin-right: 10px; vertical-align: 1px;
  }
</style>
</head>
<body>
<main class="sheet">
  <section class="card card--front" aria-label="Card front">
    <svg class="front__art" viewBox="0 0 620 354" preserveAspectRatio="none" aria-hidden="true">
      <defs>
        <linearGradient id="spectrum" x1="0" x2="1" y1="0" y2="0">
          <stop offset="0" stop-color="#f6c431"/>
          <stop offset="0.3" stop-color="#e6452b"/>
          <stop offset="0.55" stop-color="#c35aa0"/>
          <stop offset="0.8" stop-color="#6c5fad"/>
          <stop offset="1" stop-color="#1a90d8"/>
        </linearGradient>
        <linearGradient id="sheen" x1="0" x2="1" y1="0" y2="0">
          <stop offset="0" stop-color="#5a5a5a"/>
          <stop offset="0.5" stop-color="#3c3c3c"/>
          <stop offset="1" stop-color="#2c2c2c"/>
        </linearGradient>
      </defs>
      <rect class="front__white" x="0" y="0" width="620" height="124" fill="var(--card-white)"/>
      <rect class="front__spectrum" x="0" y="124" width="620" height="11" fill="url(#spectrum)"/>
      <rect class="front__band" x="0" y="135" width="620" height="60" fill="var(--band-grey)"/>
      <path class="front__sheen" d="M0 186 Q 200 140 620 142 L620 150 Q 260 150 0 190 Z" fill="url(#sheen)"/>
      <path class="front__base" d="M0 192 Q 240 158 620 162 L620 354 L0 354 Z" fill="var(--card-black)"/>
    </svg>
    <div class="brand-name">K &amp; R Coat</div>
    <div class="person-name">Darren Hollis</div>
    <ul class="contact">
      <li>
        <svg viewBox="0 0 24 24" aria-hidden="true"><path d="M3 8c0-2 4-4 9-4s9 2 9 4v2h-5V8H8v2H3zM7 11h10l3 6v3H4v-3zm5 2a2.5 2.5 0 1 0 0 5 2.5 2.5 0 0 0 0-5z"/></svg>
        <span>630-555-0148</span>
      </li>
      <li>
        <svg viewBox="0 0 24 24" aria-hidden="true"><path fill="none" stroke="var(--icon-grey)" stroke-width="2" d="M12 3a9 9 0 1 0 0 18 9 9 0 0 0 0-18zM3 12h18M12 3c3 3 3 15 0 18M12 3c-3 3-3 15 0 18M5 7h14M5 17h14"/></svg>
        <span>krcoatfoamsealers.com</span>
      </li>
    </ul>
  </section>

  <section class="card card--back" aria-label="Card back">
    <div class="brand-name">K &amp; R Coat</div>
    <ul class="services">
      <li>foam insulation</li>
      <li>waterproofing roof system</li>
      <li>water proofing foundation systems</li>
    </ul>
  </section>
</main>
</body>
</html>
```